Family Conference for a Church needs a creative & colorful flyer

We need a flyer that depicts the following information to be uploaded to our church website and church facebook in order to draw maximum attention. The image should be jpg format so that it can be easily uploaded.
Information to be added in the flyer: Please be creative !!!
1. The Second Annual
2. VARESH ANTO ( this is our brand name of the conference so please be creative in exhibiting this out )
3. Parish Family Conference
4. Growing together in Christ
5. One Church One Family One Vision
6. Presiding Spiritual Father : His Grace Dr. Theodoric Bel Ushan
7. Join us for WORSHIP, RETREAT MESSAGE, INTERACTIVE SESSIONS, WORKSHOPS
8. Save the date : Saturday November 2, 2013
9. CONTACT: Rev. Fr. K.R. Tomlan HLTRC 2857 Penderwick Lane, Bensalem PA 19387
I have uploaded a flyer called ONE for your guide only. Use that as your reference, for example ONE is VARESH ANTO for our flyer. I want my flyer to be better than that.
Second upload is a picture which I would like to be added to the flyer as a watermark effect but at the same time visible like a black & white picture or what ever is the best that you feel.
The flyer should be printable and be easily uploaded to facebook. ( jpg image )
Church people of all ages
Church

```html
<!DOCTYPE html>
<html lang="en">
<head>
<meta charset="utf-8">
<title>Varesh Anto Parish Family Conference</title>
<link href="https://fonts.googleapis.com/css2?family=Cinzel:wght@400;600;700;900&display=swap" rel="stylesheet">
<style>
:root{
  --sky-top:#f6f0c2;
  --sky-mid:#c9c38a;
  --sky-low:#6e7458;
  --field-dark:#3c3a2c;
  --field-mid:#5b5236;
  --field-gold:#a8822f;
  --gold-light:#f7e3a0;
  --gold:#c99a2e;
  --gold-deep:#7a4d12;
  --cream:#fff6d8;
  --yellow:#f3e48a;
  --white:#ffffff;
  --ink:#2a2210;
  --band:rgba(30,30,30,.55);
}
*{margin:0;padding:0;box-sizing:border-box}
html,body{width:816px;height:1200px;overflow:hidden;background:#222}
.flyer{position:relative;width:816px;height:1200px;overflow:hidden;font-family:"Cinzel",serif;text-align:center}
.sky{position:absolute;left:0;top:0;width:816px;height:520px;
  background:radial-gradient(ellipse 420px 300px at 420px 60px,var(--white),rgba(255,255,255,0) 70%),
  linear-gradient(180deg,var(--sky-top) 0%,var(--sky-mid) 45%,var(--sky-low) 100%)}
.congregation{position:absolute;left:0;top:470px;width:816px;height:140px;
  background:linear-gradient(180deg,rgba(110,100,80,0) 0%,#5d5448 30%,#4a4038 70%,#3e3a30 100%)}
.field{position:absolute;left:0;top:600px;width:816px;height:600px;
  background:linear-gradient(180deg,#4a4a3c 0%,var(--field-dark) 30%,var(--field-mid) 62%,var(--field-gold) 100%)}
.abs{position:absolute;left:0;width:816px;white-space:nowrap}
.annual{top:28px;left:42px;width:auto;font-size:36px;font-weight:700;color:var(--ink);text-align:left}
.brand{position:absolute;left:0;top:0;width:816px;height:470px}
.brand-word{font-family:"Cinzel",serif;font-weight:700;fill:url(#goldFill);stroke:#5a3a0c;stroke-width:1.5;
  filter:drop-shadow(4px 5px 4px rgba(0,0,0,.55))}
.subtitle{top:440px;font-size:50px;font-weight:700;line-height:1;
  background:linear-gradient(180deg,var(--cream),var(--gold) 90%);
  -webkit-background-clip:text;background-clip:text;color:transparent;
  filter:drop-shadow(2px 3px 2px rgba(0,0,0,.6))}
.motto-band{position:absolute;left:0;top:596px;width:816px;height:64px;background:var(--band)}
.motto{top:606px;font-size:34px;font-weight:600;color:var(--yellow)}
.tagline{top:672px;font-size:44px;font-weight:600;color:var(--white)}
.invite{top:736px;font-size:30px;font-weight:600;color:var(--white);line-height:36px}
.rule{position:absolute;height:6px;background:linear-gradient(180deg,var(--cream),var(--gold));}
.role{top:822px;font-size:28px;font-weight:600;color:var(--white)}
.father{top:866px;font-size:37px;font-weight:600;color:var(--white)}
.date{font-weight:600;line-height:1;
  background:linear-gradient(180deg,var(--cream) 10%,var(--gold) 70%,var(--gold-deep));
  -webkit-background-clip:text;background-clip:text;color:transparent;
  filter:drop-shadow(2px 3px 2px rgba(0,0,0,.5))}
.day{top:918px;left:56px;width:auto;font-size:76px;text-align:left}
.when{top:986px;font-size:80px}
.contact{position:absolute;left:78px;top:1076px;width:662px;height:62px;background:rgba(215,200,130,.5);
  color:var(--white);font-size:17px;font-weight:600;font-style:normal;line-height:24px;padding-top:7px;
  text-shadow:1px 1px 2px rgba(0,0,0,.6)}
</style>
</head>
<body>
<main class="flyer">
  <div class="sky" role="img" aria-label="Bright golden sky with sun rays breaking through clouds"></div>
  <div class="field" role="img" aria-label="Golden wheat field under a cloudy sky"></div>
  <div class="congregation" role="img" aria-label="Congregation standing in church pews with a red carpet aisle"></div>

  <p class="abs annual">The Second Annual</p>
  <h1>
    <svg class="brand" viewBox="0 0 816 470" aria-label="Varesh Anto">
      <defs>
        <linearGradient id="goldFill" x1="0" y1="0" x2="0" y2="1">
          <stop offset="0" stop-color="#f7e3a0"/>
          <stop offset="0.45" stop-color="#c99a2e"/>
          <stop offset="1" stop-color="#7a4d12"/>
        </linearGradient>
      </defs>
      <text class="brand-word" x="46" y="204" font-size="200" textLength="724" lengthAdjust="spacingAndGlyphs">VARESH</text>
      <text class="brand-word" x="48" y="440" font-size="330" textLength="722" lengthAdjust="spacingAndGlyphs">ANTO</text>
    </svg>
  </h1>
  <h2 class="abs subtitle">Parish Family Conference</h2>

  <div class="motto-band"></div>
  <p class="abs motto">One Church | One Family | One Vision</p>
  <p class="abs tagline">Growing together in Christ</p>
  <p class="abs invite">Join us for WORSHIP, RETREAT MESSAGE,<br>INTERACTIVE SESSIONS, AND WORKSHOPS</p>

  <div class="rule" style="left:0;top:836px;width:155px"></div>
  <div class="rule" style="left:660px;top:836px;width:156px"></div>
  <p class="abs role">Presiding Spiritual Father</p>
  <p class="abs father">His Grace Dr. Theodoric Bel Ushan</p>

  <p class="abs date day">Saturday</p>
  <p class="abs date when">November 2, 2013</p>

  <div class="rule" style="left:78px;top:1064px;width:662px"></div>
  <address class="contact">Rev. Fr. K.R. Tomlan HLTRC<br>2857 Penderwick Lane, Bensalem PA 19387</address>
</main>
</body>
</html>
```